Special Gift Box Design for Torvel Ridge Roasters Vietnam

We need a design for a coffee gift box - the design should reflect the premium quality of our coffee products - it should look elegant, classic, stylish, luxury. We will mostly use the box as a present for our main customers and business partners and sell it in our coffee shops.
The dimensions of the box are 26x10.5x9cm (LxWxH). The Box will contain one bag of coffee (250g) and one Vietnamese coffee filter.
We are a coffee producer in the Central Highlands of Vietnam with a sustainable, fair and inclusive business model. We are producing Arabica coffee from farm to cup. We are sourcing our coffee cherries directly from local farmers which are members of an ethnic minority. Besides Arabica and Specialty Arabicas, we also produce Robusta, blends and herbal coffees with Ginseng and Ganoderma. Our products are sold to 4 and 5-star hotels, in online and retail shops in Vietnam and we will soon start to export our coffee to other countries in Asia and overseas.
We are Greenleaf Compact certified and have received many awards (golden brand of Vietnam, special product from Dalat, typical rural industrial product of Central Vietnam etc.) for our outstanding product quality and our socially responsible business concept. We are a member of the Premium Bean Federation (PBF) and a certified PBF roaster. We are creating stable jobs in a remote and poor area of the Central Highlands.

Target Market(s)

For now Vietnam and Thailand, but later also oversea markets, so it should be an international design which can (but no must) have asian/vietnamese elements

Industry/Entity Type

Agriculture, coffee producer

Requirements
Must have
• Our logo must be prominently displayed on the box, otherwise no text or product information will be on the box for now.

```html
<!DOCTYPE html>
<html lang="en">
<head>
<meta charset="utf-8">
<title>Torvel Ridge Roasters – Gift Box Dielines</title>
<link rel="stylesheet" href="https://fonts.googleapis.com/css2?family=Oswald:wght@500&family=Ubuntu:wght@500;700&family=Arimo&display=swap">
<style>
  :root {
    --red: #c40000;
    --black: #030304;
    --cream: #ead8a4;
    --sand: #e8d198;
    --kraft: #ad9455;
    --olive: #2e2a15;
    --green: #1f7a2a;
    --ink: #111;
    --white: #fff;
    --label: #111;
  }
  * { box-sizing: border-box; margin: 0; padding: 0; }
  html, body { width: 1177px; height: 1200px; overflow: hidden; background: var(--white); }
  .canvas { position: relative; width: 1177px; height: 1200px; }
  .abs { position: absolute; }
  .view-title {
    position: absolute; top: 0; transform: translateX(-50%);
    font: 17px/1 "Arimo", sans-serif; color: var(--label); white-space: nowrap;
  }
  .fold { position: absolute; left: 0; right: 0; height: 1px; background: rgba(255,255,255,.25); }

  /* outside panel */
  .outside { left: 0; top: 31px; width: 571px; height: 628px; background: var(--black); }
  .outside .lid-top { position: absolute; left: 0; top: 0; width: 100%; height: 99px; background: var(--red); }
  .outside .lid-bottom { position: absolute; left: 0; bottom: 0; width: 100%; height: 15px; background: var(--red); }
  .side-pattern { position: absolute; top: 0; bottom: 0; width: 26px; background: linear-gradient(90deg, var(--olive), #4a4220 50%, var(--olive)); opacity: .85; }

  /* brand mark */
  .mark {
    position: absolute; transform: translate(-50%, -50%);
    display: flex; align-items: center; gap: .28em;
    font-family: "Oswald", sans-serif; font-weight: 500; line-height: .95;
    text-transform: uppercase; white-space: nowrap;
  }
  .mark-dot { width: 1.5em; height: 1.5em; border-radius: 50%; background: var(--red); flex: none; }
  .mark-name { font-size: 1em; letter-spacing: .01em; }
  .mark-sub { font-size: .48em; letter-spacing: .02em; margin-top: .12em; }
  .mark--light { color: var(--cream); }
  .mark--dark { color: var(--ink); }

  /* inside panel */
  .inside { left: 604px; top: 31px; width: 571px; height: 628px; background: var(--red); color: var(--ink); }
  .message {
    position: absolute; left: 158px; top: 222px; width: 320px; transform: translateX(-50%);
    text-align: center; font-family: "Ubuntu", sans-serif; font-weight: 500;
  }
  .message .lead { font-size: 8.5px; font-weight: 700; margin-top: 12px; }
  .message .lead:first-child { margin-top: 0; }
  .message .body { font-size: 6px; line-height: 1.65; }
  .message .thanks { font-size: 9.2px; font-weight: 700; line-height: 1.2; margin-top: 22px; }
  .message .thanks + .thanks { margin-top: 8px; }
  .partners {
    position: absolute; left: 343px; top: 238px; width: 166px; height: 87px;
    background: var(--white); border-radius: 2px;
  }
  .partners .p-shape { position: absolute; }
  .funding-note {
    position: absolute; left: 425px; top: 340px; width: 230px; transform: translateX(-50%);
    text-align: center; font-family: "Ubuntu", sans-serif; font-weight: 700; font-size: 4.6px; line-height: 1.35;
  }
  .funding-note hr { border: 0; border-top: .6px solid var(--ink); margin: 3px 0; }

  /* sleeves */
  .sleeve { position: absolute; width: 1032px; height: 195px; background: var(--sand); }
  .sleeve-1 { left: 75px; top: 776px; }
  .sleeve-2 { left: 72px; top: 1002px; }
  .sleeve .end { position: absolute; top: 0; width: 233px; height: 100%; background: var(--kraft); }
  .sleeve .end-left { left: 0; }
  .sleeve .end-right { right: 0; width: 231px; }
  .band-tribal { position: absolute; background: linear-gradient(180deg, #1a1a0d 0 18%, var(--red) 18% 62%, var(--green) 62% 100%); }
  .band-plain { position: absolute; background: linear-gradient(180deg, #3a3018 0 35%, #8b7a50 35% 100%); }
  .band-mid-left { left: 233px; width: 118px; }
  .band-mid-right { left: 684px; width: 117px; }
</style>
</head>
<body>
<main class="canvas">

  <p class="view-title" style="left:286px">The outside of the box</p>
  <p class="view-title" style="left:886px">The inside of the box</p>

  <!-- Outside -->
  <section class="abs outside" aria-label="Box outside">
    <div class="lid-top"></div>
    <div class="lid-bottom"></div>
    <div class="fold" style="top:200px"></div>
    <div class="fold" style="top:430px"></div>
    <div class="side-pattern" style="left:17px" role="img" aria-label="Vertical ethnic woven border pattern"></div>
    <div class="side-pattern" style="left:531px" role="img" aria-label="Vertical ethnic woven border pattern"></div>

    <div class="mark mark--light" style="left:286px; top:317px; font-size:46px">
      <span class="mark-dot"></span>
      <span><span class="mark-name">Torvel Ridge</span><br><span class="mark-sub">Roasters</span></span>
    </div>
    <div class="mark mark--light" style="left:286px; top:519px; font-size:28px">
      <span class="mark-dot"></span>
      <span><span class="mark-name">Torvel Ridge</span><br><span class="mark-sub">Roasters</span></span>
    </div>
  </section>

  <!-- Inside -->
  <section class="abs inside" aria-label="Box inside">
    <div class="fold" style="top:200px; background:rgba(0,0,0,.15)"></div>
    <div class="fold" style="top:430px; background:rgba(0,0,0,.15)"></div>

    <div class="message">
      <p class="lead">Với từng ly cà phê bạn thưởng thức,</p>
      <p class="body">bạn đang cứu những cánh rừng tuyệt đẹp tại Cao Nguyên Việt Nam.<br>
        Tham gia cùng chúng tôi và đối tác đáng tin cậy của Torvel Ridge<br>
        – Tổ chức Phát triển Veldra để tạo ra<br>
        những ly cà phê chất lượng cao nâng niu con người và thiên nhiên.</p>
      <p class="lead">With every cup of coffee you drink,</p>
      <p class="body">you are saving the beautiful rainforest in the Central Highlands of Vietnam.<br>
        So join us, and our trusted partner<br>
        – Veldra Development Network to help make a high-quality<br>
        cup of coffee that embraces human and nature.</p>
      <p class="thanks">Cảm ơn bạn vì đã đồng hành cùng chúng tôi!<br>Torvel Ridge Roasters</p>
      <p class="thanks">Thank you for being a part of the solution!<br>Torvel Ridge Roasters</p>
    </div>

    <div class="partners" aria-label="Partner badges">
      <span class="p-shape" style="left:14px; top:14px; width:40px; height:30px; background:#1c3b5a; border-radius:2px"></span>
      <span class="p-shape" style="left:62px; top:10px; width:36px; height:36px; border-radius:50%; background:#6ccf4e"></span>
      <span class="p-shape" style="left:106px; top:14px; width:48px; height:30px; background:#33a9e6; border-radius:2px"></span>
      <span class="p-shape" style="left:50px; top:56px; width:66px; height:18px; background:#d9d9d9; border-radius:2px"></span>
    </div>

    <div class="funding-note">
      <p>Sản phẩm được hỗ trợ bởi dự án Cà phê Xanh Lâm Đồng, tài trợ bởi Quỹ Khí hậu Northwind và Văn phòng Liên bang về Đối tác Khí hậu.</p>
      <hr>
      <p>This product is supported by the Green Highlands Coffee project, funded by the Northwind Climate Fund and the Federal Office for Climate Partnerships.</p>
    </div>
  </section>

  <!-- Sleeve, tribal band -->
  <section class="sleeve sleeve-1" aria-label="Sleeve with red and green band">
    <div class="end end-left"></div>
    <div class="end end-right"></div>
    <div class="band-tribal" style="left:3px; top:7px; width:230px; height:36px" role="img" aria-label="Red and green ethnic woven band"></div>
    <div class="band-tribal" style="right:0; top:7px; width:231px; height:36px" role="img" aria-label="Red and green ethnic woven band"></div>
    <div class="band-tribal band-mid-left" style="top:85px; height:29px" role="img" aria-label="Red and green ethnic woven band"></div>
    <div class="band-tribal band-mid-right" style="top:85px; height:29px" role="img" aria-label="Red and green ethnic woven band"></div>
    <div class="mark mark--dark" style="left:517px; top:99px; font-size:38px">
      <span class="mark-dot"></span>
      <span><span class="mark-name">Torvel Ridge</span><br><span class="mark-sub">Roasters</span></span>
    </div>
    <div class="mark mark--dark" style="left:117px; top:114px; font-size:25px">
      <span class="mark-dot"></span>
      <span><span class="mark-name">Torvel Ridge</span><br><span class="mark-sub">Roasters</span></span>
    </div>
    <div class="mark mark--dark" style="left:916px; top:114px; font-size:25px">
      <span class="mark-dot"></span>
      <span><span class="mark-name">Torvel Ridge</span><br><span class="mark-sub">Roasters</span></span>
    </div>
  </section>

  <!-- Sleeve, plain band -->
  <section class="sleeve sleeve-2" aria-label="Sleeve with brown pattern band">
    <div class="end end-left"></div>
    <div class="end end-right"></div>
    <div class="band-plain" style="left:3px; top:8px; width:230px; height:21px" role="img" aria-label="Brown ethnic motif band"></div>
    <div class="band-plain" style="right:0; top:8px; width:231px; height:21px" role="img" aria-label="Brown ethnic motif band"></div>
    <div class="band-plain band-mid-left" style="top:85px; height:16px" role="img" aria-label="Brown ethnic motif band"></div>
    <div class="band-plain band-mid-right" style="top:85px; height:16px" role="img" aria-label="Brown ethnic motif band"></div>
    <div class="mark mark--dark" style="left:517px; top:99px; font-size:38px">
      <span class="mark-dot"></span>
      <span><span class="mark-name">Torvel Ridge</span><br><span class="mark-sub">Roasters</span></span>
    </div>
    <div class="mark mark--dark" style="left:117px; top:114px; font-size:25px">
      <span class="mark-dot"></span>
      <span><span class="mark-name">Torvel Ridge</span><br><span class="mark-sub">Roasters</span></span>
    </div>
    <div class="mark mark--dark" style="left:916px; top:114px; font-size:25px">
      <span class="mark-dot"></span>
      <span><span class="mark-name">Torvel Ridge</span><br><span class="mark-sub">Roasters</span></span>
    </div>
  </section>

</main>
</body>
</html>
```